Sexy Flyer for Bra Sale

We a need flyer designed for promoting the brand Heron Apparel Company which has just begun selling bra's. need a flyer which can posted on Facebook and other social media websites. the flyer has to be attractive to girls/ladies between the ages 16 - 39. The company has been associated mainly with men's products and is now venturing into supplying bra's into the market. The heron company logo, the bra label design and the pictures of the bra's are attached.

Product description
Microfiber T-shirt bra with molded, lightly padded underwire cups for shaping and good support the bra also give's a fuller, uplifted shape and enhanced cleavage . Invisible seams for improved comfort. Narrow, adjustable shoulder straps and hook-and-eye fasteners at back. Available in two colors of Black & Black with Decorative Touches of Pink.

About Heron Apparel Company
The Heron Apparel Company was founded on the philosophy of design, quality and the ideals of redefining fashion. Sri Lanka is the global hub for manufacturing some of the most exclusive and fashionable products and the Heron brand aims at giving the Sri Lankan consumer access to high-quality, affordable and fashionable clothing from a trusted company and name. A company-wide devotion to high quality‚ honest values and timeless style with a twist. That’s authentic Heron. And that’s just what you’ll get‚ no matter your latitude or longitude. At Heron Apparel Company we constantly strive to build a culture just as inspiring as the people who wear our clothes…

Target Market(s)

Ladies Girls 16 -39
Selling Bra's

Industry/Entity Type

Womens Clothing

Requirements
Must have
• To be able to upload the flyer on Facebook and other social media platforms
• the flyer must include the Heron Apparel Company Logo
Nice to have
• Sexy flyer.

```html
<!DOCTYPE html>
<html lang="en">
<head>
<meta charset="utf-8">
<title>Heron Apparel Company – Women Lingerie Discount Vouchers</title>
<link rel="stylesheet" href="https://fonts.googleapis.com/css2?family=Abril+Fatface&family=Montserrat:wght@700&family=Raleway:wght@300;700&family=Lato:wght@400&display=swap">
<style>
  :root {
    --ink: #0b0b0b;
    --paper: #f1f1f1;
    --white: #ffffff;
    --photo-dark: #8d8c8b;
    --photo-light: #c9c7c5;
    --skin: #c99a7c;
    --denim: #9bb6cf;
    --brand-grey: #5d5b5c;
  }
  * { margin: 0; padding: 0; box-sizing: border-box; }
  html, body { width: 1200px; height: 640px; overflow: hidden; background: var(--white); }
  .flyer { position: relative; width: 1200px; height: 640px; overflow: hidden; }

  .panel { position: absolute; top: 0; height: 640px; }
  .panel--photo { left: 0; width: 398px;
    background:
      radial-gradient(ellipse 42% 34% at 36% 42%, var(--skin) 0%, rgba(201,154,124,0) 100%),
      radial-gradient(ellipse 36% 22% at 20% 84%, var(--denim) 0%, rgba(155,182,207,0) 100%),
      linear-gradient(160deg, var(--photo-light) 0%, var(--photo-dark) 100%); }
  .panel--light-a { left: 398px; width: 194px; background: var(--paper); }
  .panel--dark-a  { left: 592px; width: 192px; background: var(--ink); }
  .panel--light-b { left: 784px; width: 195px; background: var(--paper); }
  .panel--dark-b  { left: 979px; width: 221px; background: var(--ink); }

  .brand { position: absolute; left: 248px; top: 560px; width: 146px; text-align: right;
    font-family: 'Raleway', sans-serif; font-weight: 700; color: var(--brand-grey); line-height: 1; }
  .brand__name { display: block; font-size: 40px; letter-spacing: -0.5px; }
  .brand__sub { display: block; font-size: 14px; margin-top: 4px; }

  /* vertical headlines: anchored at bottom-left, reading upward */
  .vline { position: absolute; white-space: nowrap; line-height: 1; transform-origin: left top; }
  .vline--sans { font-family: 'Montserrat', sans-serif; font-weight: 700; color: var(--ink);
    font-size: 53px; transform: rotate(-90deg); }
  .vline--didone { font-family: 'Abril Fatface', serif; color: var(--ink);
    transform: rotate(-90deg) scaleX(0.5); }

  .didone { font-family: 'Abril Fatface', serif; color: var(--white); line-height: 1;
    display: inline-block; white-space: nowrap; transform: scaleX(0.52); }

  .stat { position: absolute; }
  .stat .didone { transform-origin: left top; }

  .copy { position: absolute; font-family: 'Lato', sans-serif; font-size: 11.2px; line-height: 15.9px;
    color: var(--white); text-align: justify; hyphens: auto; }
  .copy p + p { margin-top: 15.9px; }

  .tagline { position: absolute; left: 1003px; top: 71px; font-family: 'Raleway', sans-serif;
    font-size: 23px; line-height: 31px; color: var(--white); font-weight: 300; list-style: none; }
  .tagline .strong { font-weight: 700; }

  .discount { position: absolute; left: 979px; width: 221px; top: 440px; text-align: center; }
  .discount .didone { transform-origin: center top; display: block; }
</style>
</head>
<body>
<main class="flyer">
  <section class="panel panel--photo" role="img" aria-label="Photograph of a woman with long wavy brown hair in ripped light-blue jeans, lying on a grey backdrop with arms crossed over her chest">
    <div class="brand"><span class="brand__name">Heron</span><span class="brand__sub">apparel company</span></div>
  </section>

  <section class="panel panel--light-a"></section>
  <div class="vline vline--sans" style="left:440px; top:580px;">WOMEN LINGERIE</div>
  <div class="vline vline--didone" style="left:500px; top:580px; font-size:66px;">DISCOUNT VOUCHERS</div>

  <section class="panel panel--dark-a">
    <div class="stat" style="left:12px; top:76px;"><span class="didone" style="font-size:96px;">100%</span></div>
    <div class="stat" style="left:12px; top:158px;"><span class="didone" style="font-size:44px;">RESULTS</span></div>
    <div class="copy" style="left:18px; top:212px; width:160px;">
      <p>Lorem ipsum dolor sit mero moleamet, soluta euismod his ea, hiea munere accusamus ullamco detore rper quo, utamur signiferumque et duo. Brute inani in pro, in est audire delicata. Eos rebum dicant constituto ex, vix hinc postea molestiae ne, nam an fugit probatus suscipiantu50%</p>
      <p>offr. Dicit quaestio principes ieum ex, id est alia scriptorem definitiones. Assum legimusreferrentur nam utaudire delicata. Eos rebum dicant constituto ex, vix hinc postea molestiae ne, nam an fugit probatus suscipiantur. Dicit quaestio principes ieum ex, id est alia scriptorem definitiones. Assum</p>
    </div>
  </section>

  <section class="panel panel--light-b"></section>
  <div class="vline vline--didone" style="left:818px; top:540px; font-size:66px;">50 % OFFER</div>
  <div class="vline vline--didone" style="left:884px; top:536px; font-size:68px;">DISCOUNT VOUCHERS</div>

  <section class="panel panel--dark-b">
    <div class="copy" style="left:20px; top:236px; width:178px;">
      <p>Lorem ipsum dolor sit mero moleamet, soluta euismod his ea, hiea munere accusamus ullamco detore rper quo, utamur signiferumque et duo. Brute inani in pro, in est audire delicata. Eos rebum dicant constituto ex, vix hinc postea molestiae ne, nam an fugit probatus suscipiantu50%</p>
    </div>
  </section>
  <ul class="tagline">
    <li class="strong">BUSINESS</li>
    <li>INSPIRATION</li>
    <li>METION</li>
    <li class="strong">TORNA YKSI</li>
    <li>VOUCHER TO</li>
  </ul>
  <div class="discount">
    <span class="didone" style="font-size:96px;">10%</span>
    <span class="didone" style="font-size:42px; margin-top:-4px;">FLAT</span>
    <span class="didone" style="font-size:42px; margin-top:-6px;">DISCOUNT</span>
  </div>
</main>
</body>
</html>
```